CD cover "Marisol Quintero"

Here I send the pictures for the cover, leaving creative freedom to the photography and any modifications you make. The artist is called Marisol Quintero, and the title of the album is called. "Over Quiet Rivers" but please translate that to Spanish. Thank you for your valuable work.
The name of the artist is: Marisol Quintero
Album Name: “Sobre ríos quietos” in Spanish

```html
<!DOCTYPE html>
<html lang="es">
<head>
<meta charset="utf-8">
<title>Sobre ríos quietos · Marisol Quintero</title>
<link rel="stylesheet" href="https://fonts.googleapis.com/css2?family=League+Spartan:wght@600;800&display=swap">
<style>
  :root {
    --stage: #474747;
    --sky-blue: #7fa2cf;
    --sky-lilac: #c8c4da;
    --sky-peach: #f1b8a6;
    --horizon-glow: #f3e2cc;
    --grass-pale: #b7ad9c;
    --grass-olive: #7c7560;
    --ground-dark: #16120f;
    --ink-light: #ffffff;
  }
  * { margin: 0; padding: 0; box-sizing: border-box; }
  html, body {
    width: 1200px;
    height: 580px;
    overflow: hidden;
    background: var(--stage);
  }
  .canvas {
    position: relative;
    width: 1200px;
    height: 580px;
    display: flex;
    align-items: center;
    justify-content: center;
  }
  .album-cover {
    position: relative;
    width: 540px;
    height: 540px;
    overflow: hidden;
    box-shadow: 0 6px 18px rgba(0, 0, 0, 0.35);
  }
  .cover-photo {
    position: absolute;
    inset: 0;
    background:
      radial-gradient(ellipse 30% 22% at 50% 52%, rgba(255, 246, 228, 0.75), rgba(255, 246, 228, 0) 100%),
      linear-gradient(180deg,
        var(--sky-blue) 0%,
        var(--sky-lilac) 24%,
        var(--sky-peach) 42%,
        var(--horizon-glow) 52%,
        var(--grass-pale) 62%,
        var(--grass-olive) 74%,
        #3a322a 86%,
        var(--ground-dark) 100%);
  }
  .cover-text {
    position: absolute;
    left: 0;
    right: 0;
    top: 380px;
    text-align: center;
    color: var(--ink-light);
    font-family: "League Spartan", "Helvetica Neue", Arial, sans-serif;
  }
  .album-title {
    font-weight: 800;
    font-size: 46px;
    line-height: 0.86;
    letter-spacing: 0.01em;
    text-transform: uppercase;
  }
  .album-title span { display: block; }
  .artist-name {
    margin-top: 24px;
    font-weight: 600;
    font-size: 14px;
    letter-spacing: 0.38em;
    text-transform: uppercase;
    padding-left: 0.38em;
  }
</style>
</head>
<body>
  <main class="canvas">
    <section class="album-cover">
      <div class="cover-photo" role="img" aria-label="Photograph: a woman in a long blue dress seen from behind, walking along a sandy path between dry grasses and a rocky hillside toward a soft pastel sunrise sky"></div>
      <div class="cover-text">
        <h1 class="album-title"><span>Sobre</span><span>Ríos Quietos</span></h1>
        <p class="artist-name">Marisol Quintero</p>
      </div>
    </section>
  </main>
</body>
</html>
```